Business Card *

A business card design
Use the logo uploaded in the brief page.
You may use placeholders in your design layouts.
I will provide the actual business card details to the winning designer.

Logo
Place for contact info (name, title, phone, email, etc)

Requirements
Must have
• Logo

```html
<!DOCTYPE html>
<html lang="en">
<head>
<meta charset="utf-8">
<title>Harrowfield Business Card</title>
<link href="https://fonts.googleapis.com/css2?family=Archivo+Black&family=Archivo:wght@700&family=Raleway:wght@500;600&family=Roboto:wght@400&display=swap" rel="stylesheet">
<style>
  :root {
    --stage: #9a9a9a;
    --grey: #929396;
    --ink: #6d6e71;
    --green: #39b54a;
    --white: #ffffff;
    --rule: #8a8a8a;
  }
  * { margin: 0; padding: 0; box-sizing: border-box; }
  html, body { width: 1200px; height: 1200px; overflow: hidden; }
  body { background: var(--stage); position: relative; }

  .card {
    position: absolute;
    top: 303px;
    width: 369px;
    height: 593px;
    overflow: hidden;
  }
  .card--front { left: 200px; background: var(--green); }
  .card--back { left: 599px; background: var(--white); text-align: center; }

  .front-band {
    position: absolute; left: 0; top: 0; width: 100%; height: 309px;
    background: var(--grey);
  }
  .front-emblem {
    position: absolute; left: 34px; top: 150px;
    width: 300px; height: 300px; border-radius: 50%;
    background: var(--white);
  }
  .wordmark {
    font-family: "Archivo Black", sans-serif;
    letter-spacing: 0.5px;
    line-height: 1;
    white-space: nowrap;
  }
  .tagline {
    font-family: "Archivo", sans-serif;
    font-weight: 700;
    letter-spacing: 3.4px;
    line-height: 1;
    white-space: nowrap;
  }
  .card--front .wordmark {
    position: absolute; left: 0; width: 100%; top: 502px;
    text-align: center; font-size: 34px; color: var(--white);
  }
  .card--front .tagline {
    position: absolute; left: 0; width: 100%; top: 546px;
    text-align: center; font-size: 11.5px; color: var(--white);
  }

  .back-emblem {
    position: absolute; left: 129px; top: 80px;
    width: 110px; height: 110px; border-radius: 50%;
    background: var(--grey);
  }
  .card--back .wordmark {
    position: absolute; left: 0; width: 100%; top: 213px;
    font-size: 32px; color: var(--grey);
  }
  .card--back .tagline {
    position: absolute; left: 0; width: 100%; top: 247px;
    font-size: 11px; color: var(--green);
  }

  .person { position: absolute; left: 0; width: 100%; top: 337px; }
  .person-name {
    font-family: "Raleway", sans-serif; font-weight: 600;
    font-size: 25px; color: var(--ink); line-height: 1;
  }
  .person-title {
    font-family: "Roboto", sans-serif; font-size: 18px;
    color: var(--green); line-height: 1; margin-top: 4px;
  }

  .icon-row {
    position: absolute; top: 396px; left: 0; width: 100%;
    display: flex; justify-content: center; align-items: center; gap: 5px;
  }
  .icon-row .rule { width: 52px; height: 1px; background: var(--rule); margin: 0 3px; }
  .icon {
    width: 25px; height: 25px; background: var(--green); border-radius: 2px;
    display: flex; align-items: center; justify-content: center;
  }

  .contact, .address {
    position: absolute; left: 0; width: 100%;
    font-family: "Roboto", sans-serif; font-size: 17px;
    color: var(--ink); line-height: 21.5px;
  }
  .contact { top: 431px; }
  .contact .accent { color: var(--green); }
  .divider {
    position: absolute; top: 506px; left: 88px; width: 194px;
    height: 1px; background: var(--rule);
  }
  .address { top: 517px; }
</style>
</head>
<body>

  <section class="card card--front">
    <div class="front-band"></div>
    <div class="front-emblem"></div>
    <div class="wordmark">HARROWFIELD</div>
    <div class="tagline">AGRICULTURE AND INDUSTRY</div>
  </section>

  <section class="card card--back">
    <div class="back-emblem"></div>
    <div class="wordmark">HARROWFIELD</div>
    <div class="tagline">AGRICULTURE AND INDUSTRY</div>

    <div class="person">
      <div class="person-name">JONATHAN SMITH</div>
      <div class="person-title">MANAGING DIRECTOR</div>
    </div>

    <div class="icon-row">
      <span class="rule"></span>
      <span class="icon">
        <svg width="15" height="15" viewBox="0 0 16 16" aria-label="Phone">
          <path d="M1 6c0-2 3-3 7-3s7 1 7 3v1h-3V5.5C10.5 5 5.5 5 4 5.5V7H1z" fill="#fff"/>
          <rect x="3" y="8" width="10" height="6" rx="1" fill="#fff"/>
        </svg>
      </span>
      <span class="icon">
        <svg width="15" height="15" viewBox="0 0 16 16" aria-label="Email">
          <rect x="1.5" y="3.5" width="13" height="9" fill="none" stroke="#fff" stroke-width="1.4"/>
          <path d="M1.5 3.5l6.5 5 6.5-5M1.5 12.5l5-4.5M14.5 12.5l-5-4.5" fill="none" stroke="#fff" stroke-width="1.2"/>
        </svg>
      </span>
      <span class="icon">
        <svg width="15" height="15" viewBox="0 0 16 16" aria-label="Website">
          <circle cx="8" cy="8" r="6.5" fill="#fff"/>
          <path d="M5 4c2 0 3 2 2 3s-2 2-1 4M10 5c1 1 2 1 3 3M9 11c1 0 2 1 1 2" fill="none" stroke="#39b54a" stroke-width="1.4"/>
        </svg>
      </span>
      <span class="rule"></span>
    </div>

    <div class="contact">
      044-123 456 789<br>
      info@webname.com<br>
      www.<span class="accent">websitename</span>.com
    </div>
    <div class="divider"></div>
    <div class="address">
      421, Address line here<br>
      45452,Country Name
    </div>
  </section>

</body>
</html>
```